The Nine Gates for Tablet Reliance - Contemporary Book Cover Design

The Nine Gates for Tablet Reliance was published in March 2019 and is available on Brimora and other platforms now. However, I am not happy with the cover.  It's a good design in some ways - I thought it would stand out and be easily recognizable. But I don't really like the color scheme and feel that a self-help book should probably use some lighter colors and that the red is too strident. The color scheme carries over into other marketing materials like the website, social media, etc. and I don't like the red and black scheme for these purposes.
It's not essential that the cover contain an endorsement like the current one but it could. Here are some endorsements:
“A must-read for anyone who is addicted to or thinks they may have a problem with digital technology. This eloquent work will also be useful to academics and clinicians exploring potential solutions. The author recognizes the similarities between smartphone addiction and other addictions, and logically applies one of the most effective known solutions for addiction - The Nine Gates.”
-- Dale Wickersham: Noted Interventionist, Keynote Speaker and Addiction Visionary
“If you suffer from digital addiction, I strongly encourage you to use this book as your road map to get you back to the real world.”
-- Thomas Quillard, Founder of Online Channel Monitor.
The back cover would have the new design / color scheme, but can have similar text, bio, author image, etc. Or we could include the endorsements there and shorten the other text.
As for the cover it could be stylized, or an image, a partial image, or whatever. I am open to suggestions. Think about what would be inviting for a person searching for help with moderating their smartphone use.
Let's add a subtitle as well "An Inner Journey to Balanced Tablet Habits"
Here is a link to the book:
https://www.brimora.example/Nine-Gates-Tablet-Reliance/dp/4086213590

Target Market(s)
General, since this issue affects almost everyone.
Colors
Designer to choose colors to be used in the design.
Look and feel

```html
<!DOCTYPE html>
<html lang="en">
<head>
<meta charset="utf-8">
<title>The Nine Gates for Tablet Reliance – Cover Spread</title>
<link rel="stylesheet" href="https://fonts.googleapis.com/css2?family=Open+Sans:ital,wght@0,400;0,600;0,700;0,800;1,400;1,600;1,700&family=Source+Sans+3:ital,wght@0,400;1,400&display=swap">
<style>
  :root {
    --canvas: #ececec;
    --ink-light: #ffffff;
    --ink-soft: #d9d6e6;
    --front-deep: #3b2a63;
    --front-mid: #4a3680;
    --front-plum: #5a2f6a;
    --back-deep: #0f0d1c;
    --back-mid: #1d1a33;
    --art-light: #eef1f6;
    --art-teal: #2fa7a4;
    --art-navy: #2c3f6a;
    --photo-warm: #6b5a3a;
    --photo-green: #3d5a2e;
  }
  * { box-sizing: border-box; margin: 0; padding: 0; }
  html, body {
    width: 1200px; height: 800px; overflow: hidden;
    background: var(--canvas);
  }
  .spread {
    position: relative; width: 1200px; height: 800px;
    display: flex; justify-content: center; align-items: center; gap: 24px;
  }
  .cover {
    position: relative; width: 467px; height: 700px; overflow: hidden;
    color: var(--ink-light);
    box-shadow: 0 10px 30px rgba(0,0,0,0.18);
  }

  /* Back cover */
  .back-cover__texture {
    position: absolute; inset: 0;
    background:
      radial-gradient(circle at 20% 30%, rgba(31,58,58,0.55), transparent 45%),
      radial-gradient(circle at 75% 70%, rgba(60,40,60,0.5), transparent 50%),
      linear-gradient(160deg, var(--back-mid), var(--back-deep));
  }
  .back-cover__content {
    position: absolute; left: 62px; right: 54px; top: 118px;
  }
  .back-cover__heading {
    font-family: "Open Sans", sans-serif; font-weight: 700; font-style: italic;
    font-size: 17px; line-height: 1.3; text-transform: uppercase; letter-spacing: 0.2px;
    margin-bottom: 16px;
  }
  .back-cover__body {
    font-family: "Open Sans", sans-serif; font-style: italic; font-weight: 400;
    font-size: 12.5px; line-height: 1.62; color: var(--ink-soft);
    margin-bottom: 14px;
  }
  .author-block { margin-top: 26px; }
  .author-block__heading {
    font-family: "Open Sans", sans-serif; font-weight: 700; font-style: italic;
    font-size: 16px; text-transform: uppercase; margin-bottom: 12px;
  }
  .author-block__row { display: flex; gap: 14px; align-items: flex-start; }
  .author-block__photo {
    flex: 0 0 128px; height: 140px; border: 5px solid var(--ink-light);
    background: linear-gradient(135deg, var(--photo-green), var(--photo-warm) 60%, var(--back-deep));
  }
  .author-block__bio {
    font-family: "Open Sans", sans-serif; font-style: italic;
    font-size: 12px; line-height: 1.6; color: var(--ink-soft);
  }
  .author-block__name {
    display: block; font-weight: 700; font-size: 15px; color: var(--ink-light);
    text-transform: uppercase; margin-bottom: 2px;
  }

  /* Front cover */
  .front-cover__texture {
    position: absolute; inset: 0;
    background:
      radial-gradient(ellipse at 45% 55%, rgba(47,111,134,0.75), transparent 55%),
      radial-gradient(ellipse at 20% 20%, rgba(70,80,160,0.6), transparent 45%),
      radial-gradient(ellipse at 85% 85%, rgba(90,47,106,0.8), transparent 50%),
      linear-gradient(170deg, var(--front-mid), var(--front-deep) 60%, var(--front-plum));
  }
  .front-cover__endorsement {
    position: absolute; top: 52px; left: 30px; right: 30px;
    font-family: "Source Sans 3", sans-serif; font-size: 17.5px; line-height: 1.3;
    text-align: center;
  }
  .front-cover__artwork {
    position: absolute; left: 155px; top: 218px; width: 157px; height: 282px;
    border-radius: 20px;
    background:
      radial-gradient(ellipse at 50% 50%, rgba(47,167,164,0.85), transparent 62%),
      linear-gradient(180deg, var(--art-light) 0%, var(--art-navy) 30%, var(--art-teal) 58%, var(--art-navy) 82%, var(--art-light) 100%);
  }
  .front-cover__title {
    position: absolute; left: 0; right: 0; top: 514px;
    font-family: "Open Sans", sans-serif; font-weight: 800; text-transform: uppercase;
    text-align: center; line-height: 1;
  }
  .front-cover__title-lead { display: block; font-size: 24px; letter-spacing: 0.5px; }
  .front-cover__title-key { display: block; font-size: 52px; letter-spacing: 0.5px; margin-top: 2px; }
  .front-cover__title-tail { display: block; font-size: 24px; letter-spacing: 1px; margin-top: 2px; }
  .front-cover__subtitle {
    position: absolute; left: 0; right: 0; top: 630px; text-align: center;
    font-family: "Source Sans 3", sans-serif; font-style: italic; font-size: 15px;
    color: var(--ink-soft);
  }
  .front-cover__author {
    position: absolute; left: 0; right: 0; bottom: 22px; text-align: center;
    font-family: "Open Sans", sans-serif; font-weight: 600; font-size: 15px;
    letter-spacing: 1px; text-transform: uppercase;
  }
</style>
</head>
<body>
<main class="spread">

  <section class="cover back-cover" aria-label="Back cover">
    <div class="back-cover__texture" role="img" aria-label="Dark background of shadowy leaves"></div>
    <div class="back-cover__content">
      <h2 class="back-cover__heading">An effective solution to Tablet Reliance from a successfull tradition</h2>
      <p class="back-cover__body">The Nine Gates are one of the most effective solutions to addiction in human history. First published in 1939, the Nine Gates have helped millions overcome addictions, including drugs, alcohol, gambling and many others. Now in this groundbreaking book they are applied to the complex and emerging problem of Tablet Reliance.</p>
      <p class="back-cover__body">Tablet Reliance is a new disorder that has burst upon an unprepared world. Millions of people crave the use of Tablets and the constant system of sensory rewards they offer. Tablets and the companies behind them are designed to promote continued and compulsive use. This technology clearly feeds on our weaknesses, and evidence suggests Tablets can be highly addictive.</p>
      <div class="author-block">
        <h3 class="author-block__heading">About the author</h3>
        <div class="author-block__row">
          <div class="author-block__photo" role="img" aria-label="Portrait photograph of the author"></div>
          <p class="author-block__bio"><span class="author-block__name">Martin Oberle</span>has many years of personal and professional experience with drug and alcohol addiction and recovery programs. He used the proven Nine Gates approach to create this guide.</p>
        </div>
      </div>
    </div>
  </section>

  <section class="cover front-cover" aria-label="Front cover">
    <div class="front-cover__texture" role="img" aria-label="Painted purple and teal brushstroke background"></div>
    <p class="front-cover__endorsement">If you suffer from digital addiction, I strongly encourage you to use this book as your road map to get you back to the real world.</p>

    <div class="front-cover__artwork" role="img" aria-label="Illustration of a tablet whose screen is a prison cell, hands gripping the bars"></div>

    <h1 class="front-cover__title">
      <span class="front-cover__title-lead">The Nine Gates for</span>
      <span class="front-cover__title-key">Tablet</span>
      <span class="front-cover__title-tail">Reliance</span>
    </h1>
    <p class="front-cover__subtitle">An Inner Journey to Balanced Tablet Habits</p>
    <p class="front-cover__author">Martin Oberle</p>
  </section>

</main>
</body>
</html>
```